Life Coach for Lawyers Business Card Design

Elegant, original, business card design for life coaching service for associate attorneys who work in big law and struggle with stress, overwhelm, and time management. Double sided design.

Target Market(s)

Women associate attorneys who work in big law and struggle with stress, overwhelm, and time management.

Industry/Entity Type

Life Coaching

Contact Information for Business Card

Marissa Pendrell
Life Coach
518.677.3941
calmbriefcounsel.net
marissa@calmbriefcounsel.net
@calmbriefcounsel (Instagram)

Font styles to use
Other font styles liked:
• Silver South font duo. See uploaded files.

Requirements
Must have
• Icons for phone, website, email, and Instagram instead of words. Specific colors used in my logo (171B2B, 421121, FFFFFF)
Nice to have
• Foil. Embossed. Feminine design.
Should not have
• Any colors other than those used in logo. See uploaded files.

```html
<!DOCTYPE html>
<html lang="en">
<head>
<meta charset="utf-8">
<title>Calm Brief Counsel – Business Card</title>
<link rel="stylesheet" href="https://fonts.googleapis.com/css2?family=Playfair+Display:wght@400;700&family=Montserrat:wght@300;400&display=swap">
<style>
  :root {
    --ink: #171B2B;
    --wine: #421121;
    --paper: #FFFFFF;
    --stage: #ECEAEB;
    --marble-light: #EFE9EB;
    --marble-mid: #D8CDD1;
    --marble-deep: #B9AAB0;
    --serif: "Playfair Display", Georgia, serif;
    --sans: "Montserrat", Arial, sans-serif;
  }
  * { box-sizing: border-box; margin: 0; padding: 0; }
  html, body {
    width: 1200px; height: 900px; overflow: hidden;
    background: var(--stage);
  }
  .canvas {
    width: 1200px; height: 900px;
    display: flex; flex-direction: column; align-items: center; justify-content: center;
    gap: 48px;
  }
  .card {
    position: relative;
    width: 640px; height: 366px;
    background: var(--paper);
    box-shadow: 0 6px 20px rgba(23, 27, 43, 0.18);
    overflow: hidden;
  }

  /* Front side */
  .card-front .marble {
    position: absolute; inset: 0;
    background:
      radial-gradient(ellipse at 20% 30%, var(--marble-light) 0%, transparent 55%),
      radial-gradient(ellipse at 75% 70%, var(--marble-light) 0%, transparent 50%),
      linear-gradient(135deg, var(--marble-mid) 0%, var(--marble-light) 35%, var(--marble-deep) 60%, var(--marble-light) 85%, var(--marble-mid) 100%);
  }
  .brand-name {
    font-family: var(--serif);
    font-weight: 400;
    color: var(--wine);
    text-transform: uppercase;
    text-align: center;
    line-height: 1.05;
  }
  .card-front .brand-name {
    position: absolute; left: 0; right: 0; top: 50%;
    transform: translateY(-50%);
    font-size: 44px;
    letter-spacing: 2px;
  }

  /* Back side */
  .card-back .brand-name {
    position: absolute; left: 44px; top: 46px;
    font-size: 28px;
    letter-spacing: 1px;
    text-align: left;
  }
  .holder {
    position: absolute; right: 44px; top: 96px;
    text-align: right;
  }
  .holder-name {
    font-family: var(--serif);
    font-weight: 700;
    font-size: 22px;
    letter-spacing: 0.5px;
    color: var(--wine);
    text-transform: uppercase;
  }
  .holder-role {
    font-family: var(--sans);
    font-weight: 300;
    font-size: 14px;
    color: var(--ink);
    margin-top: 2px;
  }
  .divider {
    position: absolute; left: 44px; right: 44px; top: 178px;
    height: 1px; background: var(--wine);
  }
  .contact-list {
    position: absolute; left: 44px; top: 214px;
    list-style: none;
  }
  .contact-list li {
    display: flex; align-items: center; gap: 12px;
    font-family: var(--sans); font-weight: 300;
    font-size: 14px; color: var(--ink);
    line-height: 1; margin-bottom: 14px;
  }
  .contact-list svg { width: 14px; height: 14px; flex: none; }
  .social-handle {
    position: absolute; right: 44px; bottom: 44px;
    display: flex; align-items: center; gap: 10px;
    font-family: var(--sans); font-weight: 300;
    font-size: 14px; color: var(--ink);
  }
  .social-handle .mark {
    width: 13px; height: 13px; background: var(--ink); border-radius: 3px;
  }
</style>
</head>
<body>
<main class="canvas">

  <section class="card card-front" aria-label="Card front">
    <div class="marble" role="img" aria-label="Soft swirling grey and mauve marble pattern"></div>
    <p class="brand-name">Calm Brief<br>Counsel</p>
  </section>

  <section class="card card-back" aria-label="Card back">
    <p class="brand-name">Calm Brief<br>Counsel</p>

    <div class="holder">
      <p class="holder-name">Marissa Pendrell</p>
      <p class="holder-role">Life Coach</p>
    </div>

    <div class="divider"></div>

    <ul class="contact-list">
      <li>
        <svg viewBox="0 0 24 24" aria-hidden="true"><path fill="#171B2B" d="M6.6 10.8a15.1 15.1 0 0 0 6.6 6.6l2.2-2.2a1 1 0 0 1 1-.25 11.4 11.4 0 0 0 3.6.57 1 1 0 0 1 1 1V20a1 1 0 0 1-1 1A17 17 0 0 1 3 4a1 1 0 0 1 1-1h3.5a1 1 0 0 1 1 1c0 1.25.2 2.45.57 3.57a1 1 0 0 1-.25 1z"/></svg>
        518.677.3941
      </li>
      <li>
        <svg viewBox="0 0 24 24" aria-hidden="true"><path fill="#171B2B" d="M2 21l21-9L2 3v7l15 2-15 2z"/></svg>
        marissa@calmbriefcounsel.net
      </li>
      <li>
        <svg viewBox="0 0 24 24" aria-hidden="true"><g fill="none" stroke="#171B2B" stroke-width="2"><circle cx="12" cy="12" r="9.5"/><ellipse cx="12" cy="12" rx="4" ry="9.5"/><path d="M2.5 12h19"/></g></svg>
        calmbriefcounsel.net
      </li>
    </ul>

    <p class="social-handle"><span>@calmbriefcounsel</span><span class="mark"></span></p>
  </section>

</main>
</body>
</html>
```